2020 Texas RVN Summit Event flyer for annual conference held in Amarillo Texas

The Power of Connection

I need a flyer to send out via email. I The flyer will depict our theme, "The Power of Connection" event dates, website and costs. Association is Texas RVN, date April 23-25, 2020, website www.texasrvn.example, Early Bird and Member discounts location Harbor Lodge, Amarillo Texas

page 2 will have sponsor info, and keynote description, can be 3 pages if absolutely necessary
: keynote speaker Martin Dorsey, Martin is a retired Coastal Roadway Patrol officer who spent more than 17 years patrolling the Silver Cove Bridge. During that time he encountered hundreds of people who were troubled and had lost hope. They were ready to jump off the bridge and end their lives. Although a trained negotiator, Dorsey also relied on his compassion, gentle voice, eye contact, and his innate ability to “listening to understand”. During his career, he encouraged more than 200 people not to jump, go over the bridge’s rail or come back to solid ground from where they had been standing precariously. These challenging, but rewarding efforts earned him the nickname, “Keeper of the Silver Cove Bridge”. Retired, Dorsey is now dedicating his life to promoting mental health awareness and suicide prevention across the globe.
Great sponsor opportunities available at www.Texasrvn.example sponsor letter attached for info on sponsor opportunities it is not necessary to include all info

i attached a mockup page 1 flyer that i really like but graphic designer did not complete this would give you an idea of what i am looking for on page 1 although it is missing a few elements

the Meridale (logo attached) is a champion sponsor, Plainsview VTO (logo attached)

Target Market(s)

law enforcement, hospitals, mental health providers, court system,

Colors

Designer to choose colors to be used in the design.

Requirements
Must have
• theme -The Power of Connection
• website
• dates
• location
• costs
Nice to have
• prefer graphic related to theme
• Meridale is a large sponsor
• need to have 2-3 pages for all info
• include info on sponsor opportunities but does not have to include all info on attachment

```html
<!DOCTYPE html>
<html lang="en">
<head>
<meta charset="utf-8">
<title>2020 Texas RVN Summit – The Power of Connection</title>
<link rel="stylesheet" href="https://fonts.googleapis.com/css2?family=Montserrat:wght@300;400;500;600;700;800&family=Great+Vibes&display=swap">
<style>
  :root {
    --navy: #101a3a;
    --navy-deep: #0a1230;
    --photo-top: #3b4a63;
    --photo-mid: #6b7d95;
    --white: #ffffff;
    --silver: #d5d9e2;
    --ink: #101a3a;
    --gold: #d4a63a;
    --red: #b8222a;
  }
  html, body { margin: 0; padding: 0; overflow: hidden; background: var(--white); }
  .flyer {
    position: relative;
    width: 851px;
    height: 1200px;
    overflow: hidden;
    background: var(--navy);
    font-family: "Montserrat", sans-serif;
    color: var(--white);
  }
  .backdrop { position: absolute; left: 0; top: 0; }
  .hero-photo {
    position: absolute; left: 0; top: 0; width: 851px; height: 560px;
    background:
      radial-gradient(ellipse at 55% 45%, var(--photo-mid) 0%, rgba(107,125,149,0) 55%),
      linear-gradient(180deg, var(--photo-top) 0%, #2c3a55 65%, var(--navy) 100%);
  }
  .badge {
    position: absolute; left: 367px; top: 142px;
    width: 116px; height: 116px; border-radius: 50%;
    background: var(--white);
    display: flex; align-items: center; justify-content: center;
    box-shadow: 0 0 0 6px var(--navy);
  }
  .badge-name { font-weight: 700; font-size: 17px; color: var(--navy); }
  .event-name {
    position: absolute; top: 566px; width: 100%; text-align: center;
    font-weight: 700; font-size: 26px; letter-spacing: 1px; margin: 0;
  }
  .theme { position: absolute; top: 612px; width: 100%; text-align: center; margin: 0; font-weight: 400; }
  .theme-main { display: block; font-size: 92px; line-height: 1; color: var(--silver); letter-spacing: -1px; }
  .theme-sub { display: block; margin-top: 2px; font-size: 74px; font-weight: 300; line-height: 1; color: var(--white); }
  .theme-sub .joiner { font-family: "Great Vibes", cursive; font-size: 66px; margin-right: 6px; }
  .speaker-line {
    position: absolute; top: 792px; width: 100%; text-align: center; margin: 0;
    font-size: 24px; font-weight: 400;
  }
  .speaker-line strong { font-weight: 700; }
  .dates { position: absolute; left: 36px; top: 826px; }
  .dates-days { font-size: 52px; font-weight: 800; line-height: 1; margin: 0; }
  .dates-month { font-size: 26px; font-weight: 700; margin: 4px 0 0; line-height: 1.1; }
  .dates-time { font-size: 13px; font-weight: 600; margin: 2px 0 0; }
  .discounts {
    position: absolute; left: 36px; top: 932px; width: 270px; margin: 0;
    font-size: 20px; font-weight: 700; line-height: 1.2;
  }
  .venue { position: absolute; left: 30px; top: 1000px; display: flex; gap: 10px; }
  .venue svg { flex: none; }
  .venue-name { margin: 0; font-size: 21px; font-weight: 800; line-height: 1.1; text-transform: uppercase; }
  .venue-address { margin: 5px 0 0; font-size: 11px; font-weight: 500; }
  .speaker-photo {
    position: absolute; left: 440px; top: 910px; width: 140px; height: 140px; border-radius: 50%;
    background: radial-gradient(circle at 50% 40%, #b7b2ab 0%, #6d6e75 60%, #3a4058 100%);
    box-shadow: 0 0 0 5px var(--white), 0 0 0 8px var(--red);
  }
  .sponsors { position: absolute; left: 615px; top: 905px; color: var(--ink); }
  .sponsors-label { margin: 0 0 22px; font-size: 14px; font-weight: 500; }
  .sponsor { display: flex; align-items: center; gap: 8px; margin: 0 0 32px; font-size: 21px; font-weight: 700; }
  .sponsor-mark { width: 22px; height: 22px; background: var(--navy); }
  .footer {
    position: absolute; left: 0; bottom: 0; width: 100%; height: 66px;
    background: var(--navy-deep);
    display: flex; align-items: center; justify-content: center;
  }
  .website { margin: 0; font-size: 24px; font-weight: 500; letter-spacing: 3px; color: var(--gold); }
</style>
</head>
<body>
<main class="flyer">
  <div class="hero-photo" role="img" aria-label="Photo of two hands reaching toward each other, in cool blue tones"></div>
  <svg class="backdrop" width="851" height="1200" viewBox="0 0 851 1200" aria-hidden="true">
    <path d="M0 420 C 250 500 600 500 851 420 L851 560 L0 560 Z" fill="var(--navy)" opacity="0.8"/>
    <path d="M851 835 C 700 870 540 865 455 890 C 385 915 372 1010 378 1134 L851 1134 Z" fill="var(--white)"/>
  </svg>

  <div class="badge"><span class="badge-name">Texas RVN</span></div>

  <h2 class="event-name">TEXAS RVN SUMMIT</h2>
  <h1 class="theme">
    <span class="theme-main">The Power</span>
    <span class="theme-sub"><span class="joiner">of</span>connection</span>
  </h1>
  <p class="speaker-line">Principal speaker: <strong>Martin Dorsey</strong></p>

  <section class="dates">
    <p class="dates-days">23-25</p>
    <p class="dates-month">APRIL 2020</p>
    <p class="dates-time">10 AM - 4:00 PM</p>
  </section>

  <p class="discounts">Early Bird and Member<br>discounts</p>

  <section class="venue">
    <svg width="30" height="42" viewBox="0 0 30 42" aria-hidden="true">
      <path d="M15 0 C6.7 0 0 6.7 0 15 C0 26 15 42 15 42 C15 42 30 26 30 15 C30 6.7 23.3 0 15 0 Z" fill="var(--white)"/>
      <circle cx="15" cy="15" r="6" fill="var(--navy)"/>
    </svg>
    <div>
      <p class="venue-name">Harbor Lodge<br>Conference Center</p>
      <p class="venue-address">1200 Lantern Street, Amarillo Texas</p>
    </div>
  </section>

  <div class="speaker-photo" role="img" aria-label="Portrait photo of keynote speaker Martin Dorsey"></div>

  <section class="sponsors">
    <p class="sponsors-label">Our sponsors:</p>
    <p class="sponsor"><span class="sponsor-mark"></span>The Meridale</p>
    <p class="sponsor">Plainsview VTO</p>
  </section>

  <footer class="footer">
    <p class="website">www.texasrvn.example</p>
  </footer>
</main>
</body>
</html>
```